Digital & Print Graphic Design templates for Comedy Club

We need new new digital & print graphic design templates for our upcoming comedy events created for use in CANVA in the following specs
Digital:
1080x1080px
1200x600px
800x400px
1920x1080px
1080x1355px
1500x500px
851x315px
Print
11x17"
22x28"
95.5x30"

Target Market(s)

18+ comedy fans

Industry/Entity Type

comedy club

Font styles to use
Sans Serif

Colors
FFF300
FFF600
FEFA6F
FFFEC7
FFFEE8
6B429C
8869AF
B7A5CE
E3DAEB
F3F0F8

Requirements
Must have
• templates must be CANVA compatible. frame for comedian photo.
Nice to have
• would like to incorporate deep purple into the design
Should not have
• do not include phone number on any templates

```html
<!DOCTYPE html>
<html lang="en">
<head>
<meta charset="utf-8">
<title>Rob Calde – Live at Grin Room</title>
<link rel="stylesheet" href="https://fonts.googleapis.com/css2?family=Anton&family=Oswald:wght@400&display=swap">
<style>
  :root {
    --yellow: #FFF300;
    --black: #0d0d0d;
    --black-soft: #1c1c1c;
    --white: #ffffff;
    --band: #f3f3f3;
    --dots: #6b6b55;
    --photo-light: #f4f2ef;
    --photo-mid: #c9a58c;
    --photo-dark: #1a1a1a;
  }
  html, body {
    margin: 0;
    padding: 0;
    width: 1200px;
    height: 1200px;
    overflow: hidden;
    background: var(--black);
  }
  .poster {
    position: relative;
    width: 1200px;
    height: 1200px;
    overflow: hidden;
    background: var(--black);
    font-family: "Anton", sans-serif;
  }
  .top-panel {
    position: absolute;
    left: 0; top: 0;
    width: 1200px; height: 602px;
    background: var(--yellow);
  }
  .light-band {
    position: absolute;
    left: 0; top: 602px;
    width: 1200px; height: 103px;
    background: var(--band);
  }
  .band-rule {
    position: absolute;
    left: 0; top: 705px;
    width: 1200px; height: 5px;
    background: var(--yellow);
  }
  .lower-panel {
    position: absolute;
    left: 0; top: 710px;
    width: 1200px; height: 490px;
    background: linear-gradient(135deg, var(--black) 0%, var(--black-soft) 50%, var(--black) 100%);
  }
  .side-strip {
    position: absolute;
    left: 1150px; top: 0;
    width: 50px; height: 711px;
    background: var(--yellow);
  }
  .dot-strip {
    position: absolute;
    background: var(--dots);
    opacity: 0.55;
  }
  .dot-strip--top { left: 531px; top: 0; width: 34px; height: 145px; }
  .dot-strip--side { left: 1156px; top: 562px; width: 38px; height: 144px; }
  .comedian-photo {
    position: absolute;
    left: 567px; top: 0;
    width: 583px; height: 809px;
    background: linear-gradient(170deg, var(--photo-light) 0%, var(--photo-mid) 45%, #5a4436 72%, var(--photo-dark) 100%);
  }
  .headliner {
    position: absolute;
    left: 73px; top: 18px;
    margin: 0;
    font-family: "Anton", sans-serif;
    font-weight: 400;
    font-size: 164px;
    line-height: 222px;
    color: var(--black);
    letter-spacing: 1px;
    text-transform: uppercase;
  }
  .date-box {
    position: absolute;
    left: 64px; top: 536px;
    width: 433px; height: 128px;
    background: var(--black);
    color: var(--white);
    display: flex;
    align-items: center;
    justify-content: center;
    font-family: "Anton", sans-serif;
    font-size: 60px;
    letter-spacing: 1px;
  }
  .date-rule {
    position: absolute;
    left: 497px; top: 600px;
    width: 70px; height: 3px;
    background: var(--black);
    box-shadow: 0 7px 0 var(--black);
  }
  .venue-frame {
    position: absolute;
    left: 119px; top: 809px;
    width: 1100px; height: 420px;
    border: 2px solid var(--yellow);
    box-sizing: border-box;
  }
  .live-at {
    position: absolute;
    left: 156px; top: 881px;
    margin: 0;
    font-family: "Anton", sans-serif;
    font-weight: 400;
    font-size: 134px;
    line-height: 134px;
    color: var(--white);
    text-transform: uppercase;
  }
  .venue-name {
    position: absolute;
    left: 156px; top: 1021px;
    margin: 0;
    font-family: "Oswald", sans-serif;
    font-weight: 400;
    font-size: 146px;
    line-height: 146px;
    color: var(--yellow);
    text-transform: uppercase;
  }
  .club-mark {
    position: absolute;
    left: 828px; top: 839px;
    width: 288px; height: 288px;
    border-radius: 50%;
    border: 4px solid var(--yellow);
    box-sizing: border-box;
    background: var(--black);
    display: flex;
    flex-direction: column;
    align-items: center;
    justify-content: center;
    font-family: "Anton", sans-serif;
    color: var(--yellow);
    font-size: 58px;
    line-height: 62px;
    text-transform: uppercase;
    text-align: center;
  }
</style>
</head>
<body>
  <main class="poster">
    <div class="top-panel"></div>
    <div class="light-band"></div>
    <div class="band-rule"></div>
    <div class="lower-panel" role="img" aria-label="Dark background with faint chevron texture"></div>
    <div class="side-strip"></div>
    <div class="comedian-photo" role="img" aria-label="Photo of the headlining comedian"></div>
    <div class="dot-strip dot-strip--top" role="img" aria-label="Dot grid accent"></div>
    <div class="dot-strip dot-strip--side" role="img" aria-label="Dot grid accent"></div>

    <h1 class="headliner">Rob<br>Calde</h1>
    <div class="date-rule"></div>
    <div class="date-box">4 FEBURARY</div>

    <div class="venue-frame"></div>
    <p class="live-at">Live at</p>
    <p class="venue-name">Grin Room</p>

    <div class="club-mark" aria-label="The Grin Room Comedy Club">
      <span>The</span>
      <span>Grin</span>
      <span>Room</span>
    </div>
  </main>
</body>
</html>
```